Event for Hair Salon Wigs

We are introducing a new division of our hair salon selling hair wigs. We are introducing our clients to our wig line, which are beautiful well crafted wig. These wigs are not like granny's wigs, but wigs for women who want style and are willing to pay extra for beautiful believeable wigs. The event is casual were clients and there friends will be flowing in and out during a sunday afternoon.
The postcard should reflect a nice sunny spring day, but classy not extremely colorful. If you think a photo would add to a better look to the card....let me know and I will upload some.
Thank you

I have images that was uploaded, but have not been posted to this project. I'm not sure what's going on, but please look out for them. I have been trying to communicate with customer service, but no  response thus far. The cards I have received this far I think have to much of a colored pattern, I would love it if the logo "M Lovely Wigs" took center stage, rather than the word open house. Open House is important, but I don't won't it to be bolder than "wigs." Please leave room for address labels, and if possible, the description of the event should be in little bigger text. Oh, I am open to an abstract lady rather than the images that are uploaded, but if images are used, you don't have to use them all. Believe it or not...I do like simplicity:)

```html
<!DOCTYPE html>
<html lang="en">
<head>
<meta charset="utf-8">
<title>M Lovely Wigs – Open House</title>
<link href="https://fonts.googleapis.com/css2?family=Cormorant+Garamond:ital,wght@0,500;1,400&family=Great+Vibes&display=swap" rel="stylesheet">
<style>
  :root {
    --brand-red: #e3272d;
    --ribbon-red: #e2262c;
    --paper: #ffffff;
    --ink: #1a1a1a;
  }
  * { margin: 0; padding: 0; box-sizing: border-box; }
  html, body { width: 1200px; height: 929px; overflow: hidden; background: var(--paper); }
  .postcard {
    position: relative;
    width: 1200px;
    height: 929px;
    overflow: hidden;
    background: linear-gradient(to bottom,
      var(--brand-red) 0%,
      #ee6a64 12%,
      #f7b5ae 26%,
      #fde6e2 37%,
      var(--paper) 47%);
  }
  .brand-name {
    position: absolute;
    left: 0;
    width: 100%;
    top: 398px;
    text-align: center;
    font-family: "Cormorant Garamond", serif;
    font-weight: 500;
    font-size: 104px;
    line-height: 1;
    color: var(--brand-red);
    letter-spacing: 1px;
  }
  .event-title {
    position: absolute;
    left: 352px;
    top: 598px;
    font-family: "Great Vibes", cursive;
    font-size: 66px;
    line-height: 1;
    color: var(--brand-red);
  }
  .event-details {
    position: absolute;
    left: 432px;
    top: 690px;
    font-family: "Cormorant Garamond", serif;
    font-style: italic;
    font-size: 30px;
    line-height: 1;
    color: var(--ink);
  }
  .event-details sup { font-size: 0.55em; }
  .ribbon {
    position: absolute;
    left: 0;
    top: 0;
  }
  .ribbon-text {
    position: absolute;
    left: 960px;
    top: 815px;
    width: 260px;
    transform: rotate(-27deg);
    transform-origin: center;
    text-align: center;
    font-family: "Cormorant Garamond", serif;
    font-style: italic;
    font-size: 21px;
    line-height: 1.15;
    color: var(--paper);
  }
</style>
</head>
<body>
  <main class="postcard">
    <h1 class="brand-name">M Lovely Wigs</h1>
    <p class="event-title">- Open House -</p>
    <p class="event-details">Sunday April 13<sup>th</sup>, 2014 - 11am to 3pm -</p>

    <svg class="ribbon" width="1200" height="929" viewBox="0 0 1200 929" aria-hidden="true">
      <polygon points="858,929 1200,752 1200,858 1063,929" fill="var(--ribbon-red)"/>
    </svg>
    <p class="ribbon-text">Light appetizers and Drinks<br>plus Raffles!</p>
  </main>
</body>
</html>
```